International Heavy Earthmoving Freight forwarder needs a flyer design

We need a flyer design to send out on Linkedin, Facebook, e-mail blasts, instagram etc.
We would like to announce that we have just secured a new contract offering exceptionally low shipping rates from East Coast and Gulf USA to Indonesia, Malaysia, Thailand amongst other South East Asian countries.
I would like to make it an announcement like "Hot off the press"
You can visit our instagram page for photos @haulvane
I would like the contact person on the flyer to be:
Dean Harlow
dean.harlow@haulvane.example
+1 555 014 2286
www.haulvane.example

Target Market(s)

Import and export used machinery equioment dealers. Mining companies, earthmoving contractors, freight forwarders

Font styles to use
Sans Serif

Requirements
Must have
• Logo, contact details, some photos from various Haulvane media outlets

```html
<!DOCTYPE html>
<html lang="en">
<head>
<meta charset="utf-8">
<title>Haulvane – International Freight for Heavy Machinery</title>
<link rel="stylesheet" href="https://fonts.googleapis.com/css2?family=Roboto:wght@400;500;700;900&family=Roboto+Condensed:wght@700&display=swap">
<style>
  :root {
    --backdrop: #efefef;
    --brand-red: #e81f27;
    --band-grey: #6d6e71;
    --footer-cream: #f6f5f0;
    --ink: #3a3a3a;
    --white: #ffffff;
    --photo-warm: #c8673f;
    --photo-steel: #3f4f73;
    --photo-sky: #e9e6ee;
    --photo-water: #a9b4c6;
  }
  * { box-sizing: border-box; margin: 0; padding: 0; }
  html, body {
    width: 1200px; height: 1000px; overflow: hidden;
    background: var(--backdrop);
    font-family: "Roboto", Arial, sans-serif;
  }
  .flyer {
    position: absolute; left: 150px; top: 50px;
    width: 900px; height: 900px;
    background: var(--white);
    overflow: hidden;
  }
  .hero-photo {
    position: absolute; left: 0; top: 0; width: 900px; height: 592px;
    background:
      linear-gradient(180deg, transparent 0%, transparent 70%, var(--photo-water) 100%),
      linear-gradient(100deg, var(--photo-warm) 0%, var(--photo-steel) 35%, #7a5a5c 62%, var(--photo-sky) 88%);
  }
  .announcement-badge {
    position: absolute; left: 612px; top: 0; width: 168px; height: 226px;
    background: var(--brand-red); color: var(--white);
    padding: 50px 0 0 26px;
  }
  .announcement-badge .headline {
    font-family: "Roboto Condensed", "Roboto", sans-serif;
    font-weight: 700; font-size: 58px; line-height: 52px; letter-spacing: -1px;
  }
  .announcement-badge .subline {
    display: inline-block; margin-top: 6px;
    font-weight: 500; font-size: 27px; line-height: 30px;
    border-top: 2px solid var(--white); border-bottom: 2px solid var(--white);
  }
  .title-band {
    position: absolute; left: 0; top: 592px; width: 900px; height: 46px;
    background: var(--band-grey); color: var(--white);
    text-align: center; font-weight: 700; font-size: 29px; line-height: 46px;
  }
  .offer-band {
    position: absolute; left: 0; top: 638px; width: 900px; height: 176px;
    background: var(--brand-red); color: var(--white);
    text-align: center; font-size: 18px; line-height: 23px; padding-top: 24px;
  }
  .contact-footer {
    position: absolute; left: 0; top: 814px; width: 900px; height: 86px;
    background: var(--footer-cream);
  }
  .brand-tile {
    position: absolute; left: 282px; top: 758px; width: 118px; height: 110px;
    background: var(--white); border: 4px solid #e3e3e3;
    display: flex; flex-direction: column; align-items: center; justify-content: center; gap: 10px;
  }
  .brand-tile .mark { width: 30px; height: 30px; background: var(--brand-red); }
  .brand-tile .name {
    font-weight: 700; font-size: 14px; color: var(--ink); text-transform: uppercase;
  }
  .contact-details {
    position: absolute; left: 420px; top: 826px;
    font-size: 13px; line-height: 15px; color: var(--ink);
  }
</style>
</head>
<body>
  <main class="flyer">
    <div class="hero-photo" role="img" aria-label="Photo of container ships moored under cranes at a port at dusk"></div>

    <div class="announcement-badge">
      <div class="headline">HOT<br>OFF</div>
      <div class="subline">the press</div>
    </div>

    <h1 class="title-band">International Freight for Heavy Machinery</h1>

    <p class="offer-band">
      Offering exceptionally low shipping rates from<br>
      East Coast and Gulf USA to Indonesia, Malaysia,<br>
      Thailand amongst other South East Asian countries.
    </p>

    <footer class="contact-footer"></footer>

    <div class="brand-tile">
      <span class="mark"></span>
      <span class="name">Haulvane</span>
    </div>

    <address class="contact-details" style="font-style: normal;">
      Contact: Dean Harlow, Tel: +1 555 014 2286<br>
      Email: dean.harlow@haulvane.example<br>
      www.haulvane.example
    </address>
  </main>
</body>
</html>
```